Business card for event manager / organizer "velmora tandem"

Draft of a new valuable business card for my company.
Events, personnel service providers, festivals

```html
<!DOCTYPE html>
<html lang="de">
<head>
<meta charset="utf-8">
<title>Velmora Tandem – Visitenkarte</title>
<link href="https://fonts.googleapis.com/css2?family=Montserrat:wght@500;600;800&family=Poppins:wght@300;400&display=swap" rel="stylesheet">
<style>
  :root {
    --backdrop: #3a3a3c;
    --ink: #0d0d0d;
    --paper: #ffffff;
    --accent: #ef8a23;
    --muted: #9a9a9a;
    --text-dark: #1a1a1a;
  }
  * { box-sizing: border-box; margin: 0; padding: 0; }
  html, body { width: 1200px; height: 1200px; overflow: hidden; }
  body {
    background: var(--backdrop);
    font-family: "Poppins", sans-serif;
    position: relative;
  }
  .card {
    position: absolute;
    left: 220px;
    width: 760px;
    height: 434px;
    border-radius: 28px;
    overflow: hidden;
    box-shadow: 0 14px 30px rgba(0,0,0,.45);
  }
  .card--front { top: 110px; background: var(--paper); }
  .card--back { top: 640px; background: var(--ink); }

  .front-shapes { position: absolute; inset: 0; }

  .portrait {
    position: absolute;
    left: 70px; top: 58px;
    width: 190px; height: 166px;
  }
  .owner {
    position: absolute;
    left: 40px; top: 262px;
    width: 260px;
    text-align: center;
    font-family: "Montserrat", sans-serif;
  }
  .owner__name { color: var(--accent); font-weight: 600; font-size: 24px; letter-spacing: .5px; }
  .owner__role { color: var(--paper); font-weight: 500; font-size: 15px; letter-spacing: 1px; margin-top: 4px; }

  .brand-small {
    position: absolute;
    left: 440px; top: 62px;
    display: flex; align-items: center; gap: 10px;
  }
  .brand-mark { width: 46px; height: 46px; border-radius: 50%; background: var(--accent); flex: none; }
  .brand-small__name {
    font-family: "Montserrat", sans-serif; font-weight: 800;
    font-size: 28px; color: var(--text-dark); text-transform: uppercase; line-height: 1;
  }
  .brand-small__tag { font-size: 10px; color: var(--text-dark); margin-top: 4px; font-weight: 300; }

  .contacts {
    position: absolute;
    left: 470px; top: 170px;
    list-style: none;
  }
  .contacts li {
    display: flex; align-items: center; gap: 10px;
    font-size: 15px; color: var(--text-dark); line-height: 28px;
  }
  .contacts svg { width: 16px; height: 16px; flex: none; }

  .brand-large {
    position: absolute;
    left: 150px; top: 120px;
    display: flex; align-items: center; gap: 26px;
  }
  .brand-large .brand-mark { width: 120px; height: 120px; }
  .brand-large__name {
    font-family: "Montserrat", sans-serif; font-weight: 800;
    font-size: 62px; color: var(--paper); text-transform: uppercase; line-height: 1;
  }
  .brand-large__tag { font-size: 18px; color: var(--muted); font-weight: 300; margin-top: 10px; }
  .back-bar {
    position: absolute;
    left: 400px; bottom: 64px;
    width: 300px; height: 16px;
    background: var(--accent);
  }
</style>
</head>
<body>

<section class="card card--front">
  <svg class="front-shapes" viewBox="0 0 760 434" width="760" height="434" aria-hidden="true">
    <polygon points="0,0 300,0 410,210 450,434 0,434" fill="var(--ink)"/>
    <polyline points="318,0 428,210 468,434" fill="none" stroke="var(--accent)" stroke-width="5"/>
  </svg>

  <svg class="portrait" viewBox="0 0 190 166" role="img" aria-label="Portraitfoto des Inhabers">
    <defs>
      <linearGradient id="portraitTone" x1="0" y1="0" x2="0" y2="1">
        <stop offset="0" stop-color="#6b6b6b"/>
        <stop offset="1" stop-color="#2a2a2a"/>
      </linearGradient>
    </defs>
    <polygon points="48,4 142,4 186,83 142,162 48,162 4,83" fill="url(#portraitTone)" stroke="var(--accent)" stroke-width="2"/>
  </svg>

  <div class="owner">
    <p class="owner__name">JONAS BRANDEL</p>
    <p class="owner__role">INHABER</p>
  </div>

  <div class="brand-small">
    <span class="brand-mark"></span>
    <div>
      <p class="brand-small__name">Velmora<br>Tandem</p>
      <p class="brand-small__tag">…weil jedes Fest gute Hände braucht!</p>
    </div>
  </div>

  <ul class="contacts">
    <li>
      <svg viewBox="0 0 16 16"><path d="M3 1l3 3-2 2c1 2 3 4 5 5l2-2 3 3-2 3C7 15 1 9 1 3z" fill="var(--accent)"/></svg>
      02361 4820 17 36 | 0176 482 30 19
    </li>
    <li>
      <svg viewBox="0 0 16 16" fill="none" stroke="var(--accent)" stroke-width="1.4"><circle cx="8" cy="8" r="6.5"/><ellipse cx="8" cy="8" rx="3" ry="6.5"/><line x1="1.5" y1="8" x2="14.5" y2="8"/></svg>
      www.velmora-tandem.de
    </li>
    <li>
      <svg viewBox="0 0 16 16"><rect x="1" y="3" width="14" height="10" fill="var(--accent)"/><polyline points="1,3 8,9 15,3" fill="none" stroke="#fff" stroke-width="1.3"/></svg>
      info@velmora-tandem.de
    </li>
    <li>
      <svg viewBox="0 0 16 16"><rect x="2" y="2" width="12" height="12" rx="2" fill="none" stroke="var(--accent)" stroke-width="1.5"/></svg>
      /velmoratandem
    </li>
    <li>
      <svg viewBox="0 0 16 16"><path d="M8 1a5 5 0 0 1 5 5c0 4-5 9-5 9S3 10 3 6a5 5 0 0 1 5-5z" fill="var(--accent)"/><circle cx="8" cy="6" r="2" fill="#fff"/></svg>
      Lindenweg 12, 48153 Münster
    </li>
  </ul>
</section>

<section class="card card--back">
  <div class="brand-large">
    <span class="brand-mark"></span>
    <div>
      <p class="brand-large__name">Velmora<br>Tandem</p>
      <p class="brand-large__tag">…weil jedes Fest gute Hände braucht!</p>
    </div>
  </div>
  <div class="back-bar"></div>
</section>

</body>
</html>
```